Can design for new all natural low calorie spiked lemonade

We need a clean but catchy can design for a new spiked lemonade that will be all natural, gluten free and low in calories. Open to any creative ideas ranging from designs such as using a lemonade stand to simple designs such as the example pictures that are uploaded. Looking for a can that just pops out right away on the shelf but also believe less is more as far as simplicity. The beverage is called Brightwell Spiked Lemonade, that features 3 flavors. Traditional Lemonade, Peach Lemonade and lastly Strawberry Lemonade.

Target Market(s)

21-55 years of age. 75% female, 25% male.

Colors

Designer to choose colors to be used in the design.

Requirements
Must have
• The brand name is Brightwell and it is a spiked lemonade so that should be catchy so the consumer knows what it is on first glance. Must say gluten free, all natural, and 150 calories on the front of the can. Would like some type of image on the front middle of the can. There are 3 flavors so the can should blend well with each fruit but not be different cans

```html
<!DOCTYPE html>
<html lang="en">
<head>
<meta charset="utf-8">
<title>Brightwell Spiked Lemon – Can Label</title>
<link rel="stylesheet" href="https://fonts.googleapis.com/css2?family=Open+Sans:wght@400;600;700;800&display=swap">
<style>
  :root {
    --backdrop: #f3f3f3;
    --label: #ffffff;
    --mint: #bfe1da;
    --mint-soft: #d3ebe6;
    --teal: #128a72;
    --lemon: #d9d12b;
    --lemon-soft: #e8e24a;
    --fruit-a: #f2c72a;
    --fruit-b: #7db04a;
  }
  * { margin: 0; padding: 0; box-sizing: border-box; }
  html, body {
    width: 966px; height: 1200px; overflow: hidden;
    background: var(--backdrop);
    font-family: "Open Sans", Arial, sans-serif;
  }
  .canvas { position: relative; width: 966px; height: 1200px; }
  .label {
    position: absolute; left: 183px; top: 120px;
    width: 600px; height: 960px;
    background: var(--label);
    border-radius: 18px;
    overflow: hidden;
    box-shadow: 0 6px 30px rgba(0,0,0,0.06);
  }
  .leaf { position: absolute; }
  .leaf-top-left { left: 80px; top: 120px; width: 86px; height: 96px; }
  .leaf-top-right { left: 440px; top: 110px; width: 130px; height: 100px; }
  .leaf-bottom-left { left: -10px; top: 650px; width: 100px; height: 250px; }
  .leaf-right { left: 528px; top: 568px; width: 90px; height: 170px; }

  .brand {
    position: absolute; left: 0; right: 0; top: 222px;
    text-align: center;
    font-weight: 800; font-size: 70px; letter-spacing: 1px;
    color: var(--lemon);
  }
  .flavour-band {
    position: absolute; left: 35px; top: 390px;
    width: 531px; height: 82px;
    background: var(--mint-soft);
    display: flex; align-items: center; justify-content: center;
  }
  .flavour-name {
    font-weight: 400; font-size: 56px; letter-spacing: 2px;
    color: var(--lemon);
    text-transform: uppercase;
  }
  .claim {
    position: absolute; left: 0; right: 0; top: 526px;
    text-align: center;
    font-weight: 700; font-size: 44px;
    color: var(--teal);
  }
  .fruit-image {
    position: absolute; left: 235px; top: 605px;
    width: 220px; height: 176px;
    border-radius: 48% 52% 46% 54%;
    background: radial-gradient(circle at 45% 55%, var(--fruit-a) 0%, #f5d659 50%, rgba(125,176,74,0.8) 100%);
  }
  .badge {
    position: absolute; border-radius: 50%;
    background: var(--mint);
    display: flex; flex-direction: column; justify-content: center;
    line-height: 1.3;
  }
  .badge-calories {
    left: 82px; top: 636px; width: 140px; height: 140px;
    color: var(--lemon-soft);
    font-weight: 700; font-size: 26px;
    padding-left: 18px;
  }
  .badge-gluten {
    left: 351px; top: 745px; width: 160px; height: 160px;
    color: var(--teal);
    font-weight: 700; font-size: 30px;
    padding-left: 30px;
  }
</style>
</head>
<body>
<main class="canvas">
  <section class="label">
    <svg class="leaf leaf-top-left" viewBox="0 0 86 96" role="img" aria-label="Mint leaf illustration">
      <ellipse cx="43" cy="48" rx="38" ry="46" fill="var(--mint)"/>
    </svg>
    <svg class="leaf leaf-top-right" viewBox="0 0 130 100" role="img" aria-label="Mint leaf illustration">
      <ellipse cx="65" cy="50" rx="62" ry="44" fill="var(--mint)"/>
    </svg>
    <svg class="leaf leaf-bottom-left" viewBox="0 0 100 250" role="img" aria-label="Mint leaf illustration">
      <ellipse cx="30" cy="125" rx="68" ry="122" fill="var(--mint)"/>
    </svg>
    <svg class="leaf leaf-right" viewBox="0 0 90 170" role="img" aria-label="Mint leaf illustration">
      <ellipse cx="70" cy="85" rx="66" ry="82" fill="var(--mint)"/>
    </svg>

    <h1 class="brand">BRIGHTWELL</h1>
    <div class="flavour-band"><span class="flavour-name">Spiked Lemon</span></div>
    <p class="claim">All natural</p>

    <div class="badge badge-calories"><span>150</span><span>calories</span></div>
    <div class="fruit-image" role="img" aria-label="Photo of whole and halved lemons with green leaves"></div>
    <div class="badge badge-gluten"><span>Gluten</span><span>free</span></div>
  </section>
</main>
</body>
</html>
```